Brellow Yard Goods needs a spring flyer

We are a local garden centre in Mississauga, Ontario. The product we want to promote is our disposal boxes. These are boxes that can be used to dispose cleanfill, concrete, asphalt, renovation material. Sizes range from 4 yard to 40 yard bins. They can also serve a dual purpose! When customers order a box they can also order any bulk material that we carry to go in the box and essentially get a free delivery. Example: If a customer orders a 4 yard disposal box, they can get up to 4 yards of any material we carry (soils, mulches, gravels) put in the box at the time of delivery. They will only pay the price of the box and the price of the material the delivery is FREE. We would like to see designs that use the colour green. The final design should communicate FREE delivery with box rentals and reliable service! For more information visit our website www.brellowyards-example.com

Target Market(s)

target customer for this flyer is home owners. This will be distributed by mail. Needs to standout amongst all other mail flyers!

Industry/Entity Type

Concrete

Requirements
Must have
• company phone number 905-555-0187

Must have PROMO CODE: QKPLN7390
Nice to have
• a map pin pointing our location 4182 Tundle Lane, Mississauga, Ontario Canada

```html
<!DOCTYPE html>
<html lang="en">
<head>
<meta charset="utf-8">
<title>Brellow Yard Goods – Mini Disposal Box Flyer</title>
<link href="https://fonts.googleapis.com/css2?family=PT+Serif:wght@400;700&display=swap" rel="stylesheet">
<style>
  :root {
    --green: #1b8c5c;
    --green-dark: #11803f;
    --green-frame: #1c9a63;
    --green-pale: #c5e1d3;
    --green-box: #74b096;
    --grey-oval: #c9c9c9;
    --ink: #111;
    --map-tone: #e9e6df;
    --white: #fff;
  }
  html, body { margin: 0; padding: 0; overflow: hidden; background: var(--white); }
  .flyer {
    position: relative; width: 1200px; height: 1000px; overflow: hidden;
    background: var(--white); font-family: "PT Serif", Georgia, serif; color: var(--green);
  }
  .backdrop { position: absolute; inset: 0; }
  .headline { position: absolute; left: 0; width: 1200px; text-align: center; margin: 0; font-weight: 400; }
  .headline--one { top: 98px; font-size: 52px; }
  .headline--two { top: 168px; font-size: 52px; }
  .headline--three { top: 246px; font-size: 54px; font-weight: 700; }
  .photo {
    position: absolute; width: 214px; height: 164px; border: 5px solid var(--green-frame);
    background: linear-gradient(180deg, #d9d7d2 0%, #c5c3bd 55%, #8e8b86 100%);
  }
  .photo--left { left: 57px; top: 170px; }
  .photo--right { left: 905px; top: 170px; }
  .tagline { position: absolute; left: 58px; top: 366px; margin: 0; font-size: 35px; font-weight: 400; }
  .uses { position: absolute; left: 90px; top: 418px; margin: 0; font-size: 32px; font-weight: 700; line-height: 43px; }
  .materials {
    position: absolute; left: 268px; top: 480px; width: 407px; height: 180px;
    background: var(--green-box); border: 2px solid #7a7a7a; box-sizing: border-box;
    border-radius: 0 0 0 18px;
  }
  .materials ul { list-style: none; margin: 0; padding: 6px 0 0 3px; color: var(--ink); font-size: 23.5px; line-height: 33px; }
  .sizes { position: absolute; left: 907px; top: 358px; margin: 0; font-size: 21px; line-height: 28px; }
  .offer-frame { position: absolute; left: 740px; top: 420px; }
  .offer {
    position: absolute; left: 767px; top: 445px; width: 324px; margin: 0;
    font-size: 24px; line-height: 33px; text-align: justify; text-align-last: left;
  }
  .promo { position: absolute; left: 285px; top: 705px; margin: 0; font-size: 21px; font-weight: 700; line-height: 28px; }
  .contact { position: absolute; left: 285px; top: 767px; margin: 0; font-size: 18px; line-height: 23.5px; font-style: normal; color: #2b9466; }
  .brand {
    position: absolute; left: 107px; top: 778px; width: 176px; height: 98px; border-radius: 50%;
    background: var(--white); display: flex; flex-direction: column; align-items: center; justify-content: center;
  }
  .brand__name { font-size: 16px; font-weight: 700; color: var(--green-dark); text-align: center; line-height: 19px; }
  .brand__phone { font-size: 10px; font-weight: 700; color: var(--green-dark); margin-top: 4px; }
  .map {
    position: absolute; left: 822px; top: 637px; width: 316px; height: 240px; box-sizing: border-box;
    border: 2px solid var(--green-frame); background: var(--map-tone);
  }
  .map__label { position: absolute; left: 960px; top: 815px; margin: 0; font-size: 21px; }
  .map__pin { position: absolute; left: 1017px; top: 803px; width: 16px; height: 16px; border: 2px solid var(--green); border-radius: 50%; box-sizing: border-box; }
</style>
</head>
<body>
<main class="flyer">
  <svg class="backdrop" width="1200" height="1000" aria-hidden="true">
    <polygon points="235,85 750,85 565,885 52,885" fill="var(--green-pale)"/>
    <ellipse cx="742" cy="455" rx="440" ry="245" fill="var(--grey-oval)"/>
    <polygon points="52,750 190,750 162,885 52,885" fill="var(--green-dark)"/>
  </svg>

  <h1 class="headline headline--one">need to do some works and don’t know</h1>
  <p class="headline headline--two">where to put garbage?</p>
  <p class="headline headline--three">Here’s the solution!!!</p>

  <div class="photo photo--left" role="img" aria-label="Photo of a white truck carrying an empty blue disposal box under a storage dome"></div>
  <div class="photo photo--right" role="img" aria-label="Photo of the truck with a blue disposal box filled with soil"></div>

  <h2 class="tagline">A mini disposal box!</h2>
  <p class="uses">a box can be used<br>to dispose<br>different<br>materials:</p>

  <div class="materials">
    <ul>
      <li>Clean Fill (Soil &amp; Sod)</li>
      <li>Concrete</li>
      <li>Asphalt</li>
      <li>Roofing Shingles</li>
      <li>Garbage (construction materials)</li>
    </ul>
  </div>

  <p class="sizes">Sizes range is<br>from 4 to 40 yards</p>

  <svg class="offer-frame" width="380" height="195" aria-hidden="true">
    <path d="M20,12 Q40,2 60,12 L320,12 Q340,2 360,12 Q372,30 362,50 L362,150 Q372,170 360,185 Q340,194 320,184 L60,184 Q40,194 20,185 Q8,170 18,150 L18,50 Q8,30 20,12 Z"
          fill="var(--green-box)"/>
    <rect x="28" y="24" width="324" height="150" fill="var(--grey-oval)"/>
  </svg>
  <p class="offer">If you order a box and also any bulk material, we carry to go in the box and you get a free delivery</p>

  <p class="promo">when ordering use this<br>PROMO CODE: QKPLN7390</p>
  <address class="contact">
    4182 Tundle Lane,<br>
    Mississauga, ON L5C 2R9<br>
    Tel: 905-555-0187<br>
    Fax: 905-555-0142<br>
    email: info@brellowyards-example.com
  </address>

  <div class="brand">
    <span class="brand__name">Brellow Yard Goods<br>Co. Ltd.</span>
    <span class="brand__phone">(905) 555-0187</span>
  </div>

  <div class="map" role="img" aria-label="Street map of Mississauga showing the yard location"></div>
  <span class="map__pin" aria-hidden="true"></span>
  <p class="map__label">here we are</p>
</main>
</body>
</html>
```